Landing Page for a new, High Production, farming technology

Brightfield Yield
We need a single landing page, with an email signup for more information.
We build self-contained, farming boxes out of ISO containers. These containers use hydroponics and LED lighting to provide a year round growing environment for crops. So, you could grow crops anywhere at any time of the year in any environment.
For the purpose of this site, we will be doing split testing between several different themes using different sites and keywords.
This site's focus should be providing our product to people searching for high production farming technology.
We'll be focusing on the following key words: Agriculture, aquaponics, farm, garden, hydroponics, organic food, subsistence farming, urban farming, vertical garden.
Target Market(s)
We are going to be using this page to judge that
Number of Pages Required
1 page
Look and feel
Each slider illustrates characteristics of the customer's brand and the style your logo design should communicate.

```html
<!DOCTYPE html>
<html lang="en">
<head>
<meta charset="utf-8">
<title>Brightfield Yield — The New Way of Farming</title>
<link rel="stylesheet" href="https://fonts.googleapis.com/css2?family=Poppins:wght@400;500;600&family=Open+Sans:wght@400;600&display=swap">
<style>
:root{
  --green:#5c9a69;
  --orange:#eaa468;
  --text:#4a4a4a;
  --muted:#666;
  --light-bg:#f3f3f3;
  --white:#ffffff;
  --footer:#3c3c3c;
  --footer-line:#6a6a6a;
}
*{box-sizing:border-box;margin:0;padding:0}
html,body{width:1200px;height:2932px;overflow:hidden}
body{position:relative;font-family:"Open Sans",Arial,sans-serif;color:var(--text);background:var(--white)}
.abs{position:absolute}
.heading{font-family:"Poppins",Arial,sans-serif;font-weight:500;color:var(--green);letter-spacing:3px;text-align:center;text-transform:uppercase}

/* hero */
.hero{left:0;top:0;width:1200px;height:674px;overflow:hidden}
.hero-photo{position:absolute;inset:0;background:
  radial-gradient(ellipse 300px 220px at 600px 300px,#5f8a3a 0%,rgba(95,138,58,0) 70%),
  radial-gradient(ellipse 360px 200px at 600px 560px,#8a7350 0%,rgba(138,115,80,0) 75%),
  radial-gradient(ellipse 200px 300px at 80px 330px,#6b6a4c 0%,rgba(107,106,76,0) 80%),
  linear-gradient(180deg,#bfc2bc 0%,#a7a79b 45%,#8c8676 100%)}
.hero-shade{position:absolute;inset:0;background:rgba(0,0,0,.18)}
.brand{display:flex;align-items:center;gap:10px}
.brand-mark{width:22px;height:22px;background:var(--white)}
.brand-name{font-family:"Poppins",Arial,sans-serif;font-weight:500;color:var(--white);font-size:15px;letter-spacing:3px;text-transform:uppercase;line-height:1.1}
.nav{left:475px;top:37px;display:flex;gap:30px}
.nav a{font-family:"Poppins",Arial,sans-serif;font-size:11px;color:var(--white);text-decoration:none}
.signup{left:878px;top:32px;width:112px;height:28px;border:1.5px solid var(--white);border-radius:4px;color:var(--white);font-family:"Poppins",Arial,sans-serif;font-size:11px;display:flex;align-items:center;justify-content:center}
.hero-title{left:0;width:1200px;top:282px;text-align:center;font-family:"Poppins",Arial,sans-serif;font-weight:500;color:var(--white);font-size:46px;letter-spacing:7px}
.hero-sub{left:0;width:1200px;top:340px;text-align:center;font-family:"Poppins",Arial,sans-serif;color:var(--white);font-size:12px;letter-spacing:15.5px}

/* intro */
.intro-icon{left:584px;top:776px}
.intro-title{left:0;width:1200px;top:840px;font-size:24px}
.intro-text{left:312px;width:576px;top:902px;text-align:center;font-size:16px;line-height:25.5px;color:#444}

/* products */
.products{left:0;top:1128px;width:1200px;height:719px;background:var(--light-bg)}
.products-title{left:0;width:1200px;top:1185px;font-size:24px}
.section-lede{text-align:center;font-size:10px;line-height:17px;color:var(--muted)}
.products-lede{left:315px;width:570px;top:1234px}
.product-photo{left:0;top:1296px;width:596px;height:406px;box-shadow:0 4px 10px rgba(0,0,0,.25);
  background:linear-gradient(180deg,#2f3a3c 0%,#55745a 30%,#7fb85a 45%,#4e5f5c 60%,#83bd5c 72%,#3a4846 100%)}
.product-name{left:627px;top:1360px;font-family:"Poppins",Arial,sans-serif;font-weight:500;color:var(--green);font-size:18px}
.feature-list{left:627px;top:1400px;width:362px;list-style:none}
.feature-list li{display:flex;gap:12px;height:66px;padding-top:9px;border-bottom:1px solid #dcdcdc;font-size:9.5px;line-height:14px;color:var(--muted)}
.feature-list li:last-child{border-bottom:none}
.feature-list .bullet{flex:0 0 14px;height:14px;margin-top:1px}
.slider-arrows{left:920px;top:1682px;display:flex;gap:16px}
.slider-arrows span{width:24px;height:24px;background:var(--green);display:flex;align-items:center;justify-content:center}
.find-more{left:532px;top:1757px;width:136px;height:37px;background:var(--orange);border-radius:4px;color:var(--white);font-family:"Poppins",Arial,sans-serif;font-size:11px;display:flex;align-items:center;justify-content:center}

/* solutions */
.solutions-title{left:0;width:1200px;top:1972px;font-size:24px;line-height:29px}
.solutions-lede{left:275px;width:650px;top:2054px}
.solution{width:380px;display:flex;gap:15px}
.solution svg{flex:0 0 40px}
.solution h3{font-family:"Poppins",Arial,sans-serif;font-weight:500;color:var(--green);font-size:16px;margin-bottom:6px;margin-top:-2px}
.solution p{font-size:10px;line-height:16px;color:var(--muted);width:320px}

/* cta */
.cta{left:0;top:2418px;width:1200px;height:312px;overflow:hidden}
.cta-photo{position:absolute;inset:0;background:
  radial-gradient(ellipse 260px 180px at 600px 150px,#dfe9dc 0%,rgba(223,233,220,0) 70%),
  linear-gradient(90deg,#9fc2a3 0%,#8dba95 50%,#9ec1a2 100%)}
.cta-tint{position:absolute;inset:0;background:rgba(92,154,105,.55)}
.cta-title{left:0;width:1200px;top:2494px;text-align:center;font-family:"Poppins",Arial,sans-serif;font-weight:500;color:var(--white);font-size:25px;letter-spacing:3px}
.cta-lede{left:310px;width:580px;top:2544px;text-align:center;font-size:10px;line-height:16px;color:var(--white)}
.email-field{left:391px;top:2630px;width:313px;height:36px;border:1.5px solid var(--white);border-radius:4px;color:#eef5ef;font-size:11px;padding-left:14px;display:flex;align-items:center;font-style:italic}
.submit{left:719px;top:2630px;width:92px;height:36px;border:1.5px solid var(--white);border-radius:4px;color:var(--white);font-family:"Poppins",Arial,sans-serif;font-size:12px;display:flex;align-items:center;justify-content:center}

/* footer */
.footer{left:0;top:2730px;width:1200px;height:202px;background:var(--footer)}
.footer-brand{left:211px;top:2766px}
.footer-about{left:211px;top:2812px;width:190px;font-size:8px;line-height:11px;color:#ddd}
.footer-col{top:2768px;width:96px}
.footer-col h4{font-family:"Poppins",Arial,sans-serif;font-weight:500;color:var(--white);font-size:10px;padding-bottom:6px;border-bottom:1px solid var(--footer-line);margin-bottom:9px;text-transform:uppercase}
.footer-col p{font-size:8px;line-height:11px;color:#ddd;white-space:nowrap}
.copyright{left:211px;top:2906px;font-size:8px;color:#ccc}
.social{left:938px;top:2904px;display:flex;gap:7px}
.social span{width:12px;height:12px;background:#cfcfcf;border-radius:2px}
</style>
</head>
<body>

<!-- hero -->
<section class="abs hero">
  <div class="hero-photo" role="img" aria-label="Close-up of green seedlings sprouting from a hydroponic growing cube"></div>
  <div class="hero-shade"></div>
</section>
<div class="abs brand" style="left:211px;top:32px">
  <span class="brand-mark"></span>
  <span class="brand-name">Brightfield Yield</span>
</div>
<nav class="abs nav">
  <a href="#">Home</a><a href="#">Products</a><a href="#">Why Choose</a><a href="#">About Us</a><a href="#">Contact</a>
</nav>
<div class="abs signup">Sign Up</div>
<h1 class="abs hero-title">THE NEW WAY OF FARMING</h1>
<p class="abs hero-sub">HIGH PRODUCTION FARMING TECHNOLOGY</p>

<!-- intro -->
<svg class="abs intro-icon" width="32" height="32" viewBox="0 0 32 32"><circle cx="16" cy="16" r="13" fill="none" stroke="var(--orange)" stroke-width="3"/></svg>
<h2 class="abs heading intro-title">Grow crops anywere at any time of the year</h2>
<p class="abs intro-text">This is the sample version &nbsp;of Lorem Ipsum. Proin gravida nibh vel velit auctor aliquet. Aenean sollicitudin, lorem quis bibendum auctor, nisi elit consequat ipsum, nec sagittis sem nibh id elit. Duis sed odio sit amet nibh vulputate cursus a sit amet mauris. Morbi accumsan ipsum velit. Nam nec tellus a odio tincidunt auctor a ornare odio. Sed non &nbsp;mauris vitae erat consequat auctor eu</p>

<!-- products -->
<section class="abs products"></section>
<h2 class="abs heading products-title">Our Products</h2>
<p class="abs section-lede products-lede">This is the sample version &nbsp;of Lorem Ipsum. Proin gravida nibh vel velit auctor aliquet. Aenean sollicitudin, lorem quis bibendum auctor, nisi elit consequat ipsum, nec sagittis sem nibh id elit. Duis sed odio sit amet nibh vulputate cursus a sit</p>
<div class="abs product-photo" role="img" aria-label="Interior of a container farm with racks of lettuce under LED grow lights"></div>
<h3 class="abs product-name">FARMING BOX ISO</h3>
<ul class="abs feature-list">
  <li><svg class="bullet" viewBox="0 0 14 14"><rect x="1" y="1" width="12" height="12" rx="2" fill="var(--orange)"/><path d="M4 7l2 2 4-4" stroke="#fff" stroke-width="1.5" fill="none"/></svg><span>This is the sample version &nbsp;of Lorem Ipsum. Proin gravida nibh vel velit auctor aliquet. Aenean sollicitudin, lorem quis bibendum auctor, nisi elit</span></li>
  <li><svg class="bullet" viewBox="0 0 14 14"><rect x="1" y="1" width="12" height="12" rx="2" fill="var(--orange)"/><path d="M4 7l2 2 4-4" stroke="#fff" stroke-width="1.5" fill="none"/></svg><span>This is the sample version &nbsp;of Lorem Ipsum. Proin gravida nibh vel velit auctor aliquet. Aenean sollicitudin, lorem quis bibendum auctor, nisi elit</span></li>
  <li><svg class="bullet" viewBox="0 0 14 14"><rect x="1" y="1" width="12" height="12" rx="2" fill="var(--orange)"/><path d="M4 7l2 2 4-4" stroke="#fff" stroke-width="1.5" fill="none"/></svg><span>This is the sample version &nbsp;of Lorem Ipsum. Proin gravida nibh vel velit auctor aliquet. Aenean sollicitudin, lorem quis bibendum auctor, nisi elit</span></li>
  <li><svg class="bullet" viewBox="0 0 14 14"><rect x="1" y="1" width="12" height="12" rx="2" fill="var(--orange)"/><path d="M4 7l2 2 4-4" stroke="#fff" stroke-width="1.5" fill="none"/></svg><span>This is the sample version &nbsp;of Lorem Ipsum. Proin gravida nibh vel velit auctor aliquet. Aenean sollicitudin, lorem quis bibendum auctor, nisi elit</span></li>
</ul>
<div class="abs slider-arrows">
  <span><svg width="10" height="10" viewBox="0 0 10 10"><path d="M6.5 2L3.5 5l3 3" stroke="#fff" stroke-width="1.6" fill="none"/></svg></span>
  <span><svg width="10" height="10" viewBox="0 0 10 10"><path d="M3.5 2l3 3-3 3" stroke="#fff" stroke-width="1.6" fill="none"/></svg></span>
</div>
<div class="abs find-more">Find More</div>

<!-- solutions -->
<h2 class="abs heading solutions-title">We provide best solutions for customers,<br>humanity &amp; the environment</h2>
<p class="abs section-lede solutions-lede">This is the sample version &nbsp;of Lorem Ipsum. Proin gravida nibh vel velit auctor aliquet. Aenean sollicitudin, lorem quis bibendum auctor, nisi elit consequat ipsum, nec sagittis sem nibh id elit. Duis sed odio sit amet nibh vulputate cursus a sit amet mauris. Morbi accumsan</p>

<div class="abs solution" style="left:218px;top:2142px">
  <svg width="40" height="40" viewBox="0 0 40 40"><g fill="var(--orange)"><circle cx="20" cy="20" r="12"/><rect x="17" y="4" width="6" height="32"/><rect x="4" y="17" width="32" height="6"/><rect x="17" y="4" width="6" height="32" transform="rotate(45 20 20)"/><rect x="17" y="4" width="6" height="32" transform="rotate(-45 20 20)"/></g><path d="M14 20l4 4 8-8" stroke="#fff" stroke-width="2.5" fill="none"/></svg>
  <div><h3>Innovative Systems</h3><p>This is the sample version &nbsp;of Lorem Ipsum. Proin gravida nibh vel velit auctor aliquet. Aenean sollicitudin, lorem quis bibendum</p></div>
</div>
<div class="abs solution" style="left:612px;top:2142px">
  <svg width="40" height="40" viewBox="0 0 40 40"><g fill="none" stroke="var(--orange)" stroke-width="2"><path d="M14 22a8 8 0 1 1 12 0c-2 2-2 4-2 6h-8c0-2 0-4-2-6z"/><path d="M16 32h8M17 35h6"/><path d="M20 4v3M8 10l2 2M32 10l-2 2M5 20h3M35 20h-3"/></g></svg>
  <div><h3>Intelligent Solutions</h3><p>This is the sample version &nbsp;of Lorem Ipsum. Proin gravida nibh vel velit auctor aliquet. Aenean sollicitudin, lorem quis bibendum</p></div>
</div>
<div class="abs solution" style="left:218px;top:2244px">
  <svg width="40" height="40" viewBox="0 0 40 40"><g fill="none" stroke="var(--orange)" stroke-width="2"><circle cx="20" cy="14" r="7"/><path d="M13 14h14M20 7v14"/><path d="M4 22l6 8h10M36 22l-6 8H20"/><path d="M10 30v5M30 30v5"/></g></svg>
  <div><h3>Friendly Environment</h3><p>This is the sample version &nbsp;of Lorem Ipsum. Proin gravida nibh vel velit auctor aliquet. Aenean sollicitudin, lorem quis bibendum</p></div>
</div>
<div class="abs solution" style="left:612px;top:2244px">
  <svg width="40" height="40" viewBox="0 0 40 40"><path d="M6 34C6 16 18 6 36 6c0 18-10 28-26 26z" fill="var(--orange)"/><path d="M6 34L26 14" stroke="#fff" stroke-width="2"/></svg>
  <div><h3>Organic Food</h3><p>This is the sample version &nbsp;of Lorem Ipsum. Proin gravida nibh vel velit auctor aliquet. Aenean sollicitudin, lorem quis bibendum</p></div>
</div>

<!-- cta -->
<section class="abs cta">
  <div class="cta-photo" role="img" aria-label="Soft-focus rows of young plants in a hydroponic farm"></div>
  <div class="cta-tint"></div>
</section>
<h2 class="abs cta-title">FIND MORE ABOUT OUR PRODUCTS</h2>
<p class="abs cta-lede">This is the sample version &nbsp;of Lorem Ipsum. Proin gravida nibh vel velit auctor aliquet. Aenean sollicitudin, lorem quis bibendum auctor, nisi elit consequat ipsum, nec sagittis sem nibh id elit. Duis sed odio sit amet nibh vulputate cursus a sit</p>
<div class="abs email-field">Enter you Email Address</div>
<div class="abs submit">Submit</div>

<!-- footer -->
<footer class="abs footer"></footer>
<div class="abs brand footer-brand">
  <span class="brand-mark" style="width:18px;height:18px"></span>
  <span class="brand-name" style="font-size:12px">Brightfield Yield</span>
</div>
<p class="abs footer-about">Brightfield Yield builds container farms that grow fresh crops all year. Hydroponic beds and LED light keep harvests steady in any climate, from city rooftops to remote sites and small farms.</p>
<div class="abs footer-col" style="left:479px"><h4>Company</h4><p>Home<br>Services<br>About Us</p></div>
<div class="abs footer-col" style="left:668px"><h4>Products</h4><p>Lorem Ipsum<br>Lorem Ipsum Dolor<br>Lorem Ipsum</p></div>
<div class="abs footer-col" style="left:850px"><h4>Contact</h4><p>48 Meadowline Avenue,<br>Greenvale, USA<br>60512<br>hello@brightfieldyield.com<br>0800 555 014</p></div>
<p class="abs copyright">© 2018, &nbsp;Brightfield Yield. &nbsp;All Rights Reserved.</p>
<div class="abs social"><span></span><span></span><span></span></div>

</body>
</html>
```